Brit Rock covers band "The Tin Kettles" requires poster for Marlowe Lounge Friday March 31st

I want a design for a poster (A3 and A4) and Facebook/Instagram ads.
Primary focus is the band name logo "The Tin Kettles", style as in attached file, followed by tag "Old Skool Brit Rock".
Backdrop to be 60's psychedelic art.
Secondary focus is the venue "The Marlowe Lounge"
Supporting text to include:
- 27 Fenwick Road, Chatswood SYDNEY
- Friday 31st March 2023
- 7:00 pm until late
- Bar sales refreshments
- NO admission fee

```html
<!DOCTYPE html>
<html lang="en">
<head>
<meta charset="utf-8">
<title>The Tin Kettles – The Marlowe Lounge</title>
<link rel="stylesheet" href="https://fonts.googleapis.com/css2?family=Saira+Condensed:wght@500;600;700;800&family=Saira:wght@400;500;700;800&family=Alfa+Slab+One&display=swap">
<style>
  :root {
    --ink: #0d1418;
    --white: #ffffff;
    --gold: #db9200;
    --gold-text: #e3a106;
    --teal: #1f5a5a;
    --wine: #7a2a2e;
    --ochre: #8a6a2a;
    --navy: #1c2440;
  }
  html, body {
    margin: 0;
    padding: 0;
    width: 849px;
    height: 1200px;
    overflow: hidden;
    background: var(--ink);
  }
  .poster {
    position: relative;
    width: 849px;
    height: 1200px;
    overflow: hidden;
    font-family: "Saira", sans-serif;
    color: var(--white);
  }
  .backdrop {
    position: absolute;
    inset: 0;
    background:
      radial-gradient(ellipse 32% 22% at 50% 42%, rgba(140,60,60,0.75), transparent 70%),
      radial-gradient(ellipse 45% 30% at 52% 48%, rgba(160,130,80,0.55), transparent 75%),
      radial-gradient(ellipse 40% 30% at 20% 70%, rgba(31,90,90,0.7), transparent 75%),
      radial-gradient(ellipse 40% 30% at 80% 65%, rgba(122,42,46,0.65), transparent 75%),
      radial-gradient(ellipse 35% 25% at 30% 25%, rgba(138,106,42,0.5), transparent 75%),
      radial-gradient(ellipse 35% 25% at 75% 28%, rgba(28,36,64,0.7), transparent 75%),
      radial-gradient(ellipse 80% 70% at 50% 50%, var(--teal), var(--ink) 85%);
  }
  .band-name {
    position: absolute;
    left: 0;
    right: 0;
    top: 150px;
    margin: 0;
    text-align: center;
    font-family: "Saira Condensed", sans-serif;
    font-weight: 800;
    color: var(--white);
    line-height: 0.9;
    text-transform: uppercase;
  }
  .band-name .line-1 { display: block; font-size: 104px; padding-left: 30px; }
  .band-name .line-2 { display: block; font-size: 138px; padding-left: 60px; }
  .tagline {
    position: absolute;
    left: 0;
    top: 0;
    width: 849px;
    height: 1200px;
    pointer-events: none;
  }
  .tagline text {
    font-family: "Alfa Slab One", serif;
    font-size: 33px;
    fill: var(--gold-text);
    letter-spacing: 1px;
  }
  .venue {
    position: absolute;
    left: 0;
    right: 0;
    top: 548px;
    margin: 0;
    text-align: center;
    white-space: nowrap;
    font-family: "Saira Condensed", sans-serif;
    font-weight: 700;
    font-size: 84px;
    letter-spacing: 3px;
    color: var(--white);
    text-shadow: 2px 2px 0 var(--ink), -1px -1px 0 var(--ink);
  }
  .date-pill {
    position: absolute;
    left: 90px;
    top: 700px;
    width: 668px;
    height: 105px;
    border-radius: 24px;
    background: var(--gold);
    display: flex;
    align-items: center;
    justify-content: center;
    font-family: "Saira", sans-serif;
    font-weight: 800;
    font-size: 47px;
    color: var(--ink);
    letter-spacing: 1px;
  }
  .time {
    position: absolute;
    left: 82px;
    top: 862px;
    line-height: 1;
  }
  .time .start {
    display: block;
    font-weight: 800;
    font-size: 58px;
    text-shadow: 2px 2px 0 var(--ink);
  }
  .time .until {
    display: block;
    font-weight: 400;
    font-size: 47px;
    margin-top: 2px;
    text-shadow: 2px 2px 0 var(--ink);
  }
  .divider {
    position: absolute;
    left: 348px;
    top: 863px;
    width: 5px;
    height: 110px;
    border-radius: 3px;
    background: var(--gold);
  }
  .details {
    position: absolute;
    left: 368px;
    top: 882px;
    font-weight: 500;
    font-size: 31px;
    line-height: 1.05;
    letter-spacing: 0.5px;
    text-shadow: 2px 2px 0 var(--ink);
  }
  .details span { display: block; }
  .rule {
    position: absolute;
    left: 60px;
    top: 1082px;
    width: 729px;
    height: 5px;
    border-radius: 3px;
    background: var(--gold);
  }
  .address {
    position: absolute;
    left: 0;
    right: 0;
    top: 1098px;
    text-align: center;
    font-weight: 500;
    font-size: 38px;
    letter-spacing: 0.5px;
    white-space: nowrap;
    text-shadow: 2px 2px 0 var(--ink);
  }
</style>
</head>
<body>
<main class="poster">
  <div class="backdrop" role="img" aria-label="1960s psychedelic swirling backdrop in teal, wine red, ochre and navy bands"></div>

  <h1 class="band-name">
    <span class="line-1">The Tin</span>
    <span class="line-2">Kettles</span>
  </h1>

  <svg class="tagline" viewBox="0 0 849 1200" aria-label="Old Skool Brit Rock">
    <defs>
      <path id="tagline-arc" d="M196,420 Q430,535 660,410"/>
    </defs>
    <text><textPath href="#tagline-arc" startOffset="50%" text-anchor="middle">OLD SKOOL BRIT ROCK</textPath></text>
  </svg>

  <h2 class="venue">"THE MARLOWE LOUNGE"</h2>

  <div class="date-pill">FRIDAY 31ST MARCH 2023</div>

  <div class="time">
    <span class="start">7:00 PM</span>
    <span class="until">UNTIL LATE</span>
  </div>
  <div class="divider"></div>
  <div class="details">
    <span>BAR SALES REFRESHMENTS</span>
    <span>NO ADMISSION FEE</span>
  </div>

  <div class="rule"></div>
  <div class="address">27 FENWICK ROAD, CHATSWOOD SYDNEY</div>
</main>
</body>
</html>
```